TRV Medicaid and Estate Planning

Improve look and feel of existing content. Create consistency between website and brochure aesthetics/theme.

The average monthly cost for a nursing home is about $5,000. Most people cannot afford that. As a result, roughly 65% of all nursing home residents turn to Medicaid to finance their medical care. Medicaid is a state and federally funded Title 19 benefit program, and most people recognize Medicaid as a program to help poor people. But, fewer people recognize Medicaid as a program that can help most middle class families to preserve their wealth and even pass an inheritance—all the while receiving Medicaid benefits to cover the costs of long term care.

Marcus L. Doyle
Texas
mdoyle@trvlawgroup.example
(555) 248-3071 x204
Due to a lack of understanding or possibly a stigmatization of “receiving benefits,” a lot of families pay the nursing home from their life savings. But $60,000 a year as a private pay patient will quickly expend most people’s life savings. The next step is usually to sell the family home to continue paying privately. The hard truth is none of that is necessary with proper Medicaid planning. An unfortunate reality is that a great number of families who could have benefitted from Medicaid planning will eventually end up turning to Medicaid when they have exhausted all other resources.

But wouldn’t it be nice to pass an inheritance to the grandchildren? Or, to provide for a special needs child? What about preserving the life savings entirely? These are some of the things an elder law attorney can help with. The Medicaid qualification criteria and its governing law is complex, but it was written with numerous provisions that allow for the protection of the family.

Seventy percent of those over 65 years old will need some form of long term care in their lifetimes. If you or someone you love is within that 70%, consult with an elder law attorney to see what planning options you may have.

Don’t Go Bankrupt Paying a Nursing Home

If your loved one needs long term care, but you cannot afford the cost of a nursing home, what do you do? People all across Texas are asking themselves this same question. The number one payer source for long term care is Medicaid—not long term care insurance, not Medicare, not life savings. So, the question is: are you eligible for nursing home Medicaid?

For a free legal consultation, contact us at (555) 613-8842 or mdoyle@trvlawgroup.example.

http://www.trvlawgroup.example/estate-planning/medicaid-nursing-homes-and-estate-planning/

Target Market(s)

Texas, Colorado, Elder Law and Estate Planning interests

Font styles to use
Serif

Requirements
Must have
• content I submitted

```html
<!DOCTYPE html>
<html lang="en">
<head>
<meta charset="utf-8">
<title>TRV Medicaid and Estate Planning – Brochure and Rack Card</title>
<link rel="stylesheet" href="https://fonts.googleapis.com/css2?family=Open+Sans:ital,wght@0,400;0,600;0,700;1,400;1,700&family=Libre+Baskerville:wght@700&family=Oswald:wght@300&display=swap">
<style>
:root{
  --navy:#1c2452;
  --orange:#e87722;
  --green:#1f3b25;
  --tan:#c9b27a;
  --gold:#f5a81c;
  --board:#bdbec0;
  --ink:#222a44;
  --white:#ffffff;
  --sky:#3f7fc4;
}
*{box-sizing:border-box;margin:0;padding:0}
html,body{width:1138px;height:1200px;overflow:hidden}
body{background:var(--board);font-family:"Open Sans",Arial,sans-serif;color:var(--ink);position:relative}
.sheet{position:absolute;background:var(--white)}
.abs{position:absolute}
.stripe{height:5px;background:linear-gradient(90deg,var(--orange) 0 20%,var(--green) 20% 40%,var(--tan) 40% 60%,var(--gold) 60% 80%,var(--navy) 80% 100%)}
.stripe-4{height:7px;background:linear-gradient(90deg,var(--orange) 0 25%,var(--green) 25% 50%,var(--tan) 50% 75%,var(--gold) 75% 100%)}
.body-copy{font-size:7px;line-height:1.5}
.body-copy p+p{margin-top:7px}
.centered{text-align:center}
.phone{font-weight:700;font-style:italic;color:var(--gold);font-size:13px;letter-spacing:.3px}
.navy-band{background:var(--navy);display:flex;align-items:center;justify-content:center}
.brand{text-align:center;font-family:"Libre Baskerville",Georgia,serif;color:#4a4a4a;font-weight:700;line-height:1}
.brand .mark{display:block;font-size:54px;letter-spacing:-1px}
.brand .name{display:block;font-size:6px;margin-top:4px;letter-spacing:.5px}
.photo{position:absolute}
.orange-band{background:var(--orange);color:var(--white);font-family:"Oswald",Arial,sans-serif;font-weight:300;font-size:12.5px;line-height:1.25;text-align:center;display:flex;align-items:center;justify-content:center}
.accent{color:var(--orange)}
.contact{display:flex;justify-content:space-between;font-size:6.6px;line-height:1.5;padding:9px 12px 0}
.cheat{border:1px solid var(--tan);padding:6px 8px;font-size:6.8px}
.cheat table{width:100%;border-collapse:collapse}
.cheat td{padding:3.6px 0;text-align:right}
.cheat td.val{width:52px;padding-left:10px;text-align:left}
.heading-sm{font-weight:700;font-size:10px;color:var(--navy)}
.myths{color:var(--white);font-size:7px;line-height:1.5}
.myths .myth{color:var(--gold);font-style:italic;margin-top:10px}
.myths .myth::before{content:"■";font-style:normal;font-size:5px;margin-right:6px;vertical-align:1px}
.col-head{font-weight:700;font-size:7.2px;color:var(--navy)}
</style>
</head>
<body>

<!-- Outside spread -->
<section class="sheet" style="left:42px;top:39px;width:699px;height:539px">
  <!-- Panel: attorney intro -->
  <div class="abs stripe" style="left:11px;top:16px;width:200px"></div>
  <h2 class="abs" style="left:15px;top:40px;width:210px;font-size:9.6px;line-height:1.55;font-weight:700;color:var(--navy)">ATTORNEY MARCUS DOYLE HAS ASSISTED HUNDREDS OF FAMILIES QUALIFY FOR MEDICAID BENEFITS TO COVER THE COST OF LONG TERM CARE.</h2>
  <div class="photo" role="img" aria-label="Photo of smiling senior couples giving thumbs up" style="left:0;top:106px;width:233px;height:195px;background:linear-gradient(135deg,#e9ded3,#c9a88e 50%,#8a6c5c)"></div>
  <div class="abs body-copy" style="left:17px;top:316px;width:205px">
    <p>Sometimes families do not need the assistance of an elder law attorney. Sometimes nursing facilities can assist residents apply for benefits.</p>
    <p>But, sometimes families have properties out of state, have earnings above the income cap, or have business interests or promissory notes. Sometimes families just want to protect the family nest egg, or to protect the spouse who is not in the nursing home, or to protect against unexpected surprises that may lead to an eligibility denial.</p>
    <p>In these cases, these families need an elder law attorney to protect them. They need attorney Marcus Doyle. Contact Tolliver, Reyes &amp; Vance today.</p>
  </div>
  <div class="abs navy-band" style="left:0;top:493px;width:233px;height:39px"><span class="phone">555 - 248 - 3071 Ext. 204</span></div>
  <div class="abs stripe-4" style="left:0;top:532px;width:233px"></div>

  <!-- Panel: cheat sheet -->
  <div class="abs stripe" style="left:246px;top:16px;width:208px"></div>
  <div class="abs body-copy centered" style="left:245px;top:35px;width:210px">
    <p>If your loved one needs long term care, but you cannot afford the cost of a nursing home, what do you do? People all across Texas are asking themselves this same question.</p>
    <p>The number one payer source for long term care is Medicaid—not long term care insurance, not Medicare, not life savings.</p>
    <p>So, the question is: are you eligible for nursing home Medicaid? Find out with a free legal consultation.</p>
  </div>
  <div class="abs brand" style="left:233px;top:180px;width:233px">
    <span class="mark">TRV</span>
    <span class="name">TOLLIVER REYES &amp; VANCE</span>
  </div>
  <h3 class="abs centered" style="left:233px;top:304px;width:233px;font-size:10px;font-weight:600;color:var(--navy)">Quick Reference Cheat Sheet</h3>
  <div class="abs cheat" style="left:243px;top:323px;width:213px">
    <table>
      <tr><td>Monthly Income Cap (single)</td><td class="val">$2,205</td></tr>
      <tr><td>Monthly Income Cap (2 spouses in care)</td><td class="val">$4,410</td></tr>
      <tr><td>Countable Asset Cap (single)</td><td class="val">$2,000</td></tr>
      <tr><td>Countable Asset Cap (2 spouses in care)</td><td class="val">$3,000</td></tr>
      <tr><td>Spousal Protected Resource Amount, Min.</td><td class="val">$24,180</td></tr>
      <tr><td>Spousal Protected Resource Amount, Max.</td><td class="val">$120,900</td></tr>
      <tr><td>Minimum Maintenance Needs Allowance</td><td class="val">$3022.50</td></tr>
      <tr><td>Transfer Penalty Divisor</td><td class="val">$162.41</td></tr>
    </table>
  </div>

  <!-- Panel: cover -->
  <div class="abs brand" style="left:466px;top:18px;width:233px">
    <span class="mark" style="font-size:60px">TRV</span>
    <span class="name">TOLLIVER REYES &amp; VANCE</span>
  </div>
  <div class="photo" role="img" aria-label="Illustration of a stethoscope resting on a blue map of the southern United States" style="left:466px;top:135px;width:233px;height:154px;background:linear-gradient(135deg,#cdd9ea,#5d8fcc 45%,#2c5a9a 75%,#1e3560)"></div>
  <div class="abs orange-band" style="left:466px;top:290px;width:233px;height:46px">MINERAL. INTELLECTUAL. RESIDENTIAL.<br>COMMERCIAL. PROPERTY</div>
  <div class="abs body-copy centered" style="left:476px;top:352px;width:213px">
    <p>Don’t know how to pay for long term care? For starters, don’t pay more than you need to for legal advice. Call to make an appointment with <span class="accent">Marcus Doyle</span> at TRV today.</p>
  </div>
  <div class="abs stripe" style="left:478px;top:404px;width:208px"></div>
  <div class="abs body-copy centered" style="left:476px;top:416px;width:213px">
    <p>Call for an appointment at our Midtown address. We will also meet you on your terms, whether at a nursing facility or a place of your choosing.</p>
  </div>

  <div class="abs navy-band" style="left:233px;top:459px;width:466px;height:34px;justify-content:space-around"><span class="phone">555 - 248 - 3071 Ext. 204</span><span class="phone">555 - 248 - 3071 Ext. 204</span></div>
  <div class="abs contact" style="left:233px;top:493px;width:233px;font-size:6.2px"><div>Visit us on the web at<br>www.trvlawgroup.example<br>email: mdoyle@trvlawgroup.example</div><div>Bayline Commerce Center<br>872 Alder St., Suite 310<br>Houston, TX 77099</div></div>
  <div class="abs contact" style="left:466px;top:493px;width:233px;font-size:6.2px"><div>Visit us on the web at<br>www.trvlawgroup.example<br>email: mdoyle@trvlawgroup.example</div><div>Bayline Commerce Center<br>872 Alder St., Suite 310<br>Houston, TX 77099</div></div>
</section>

<!-- Inside spread -->
<section class="sheet" style="left:42px;top:610px;width:699px;height:539px">
  <!-- Myths panel -->
  <div class="abs" style="left:0;top:0;width:233px;height:539px;background:var(--navy)"></div>
  <div class="abs" style="left:0;top:0;width:233px;height:103px;background:linear-gradient(180deg,#ffffff 70%,#e7ebf3)"></div>
  <svg class="abs" style="left:15px;top:22px" width="48" height="48" viewBox="0 0 48 48" aria-hidden="true"><circle cx="24" cy="24" r="23" fill="var(--sky)"/></svg>
  <div class="abs" style="left:73px;top:24px;color:#2566b0;line-height:1.1">
    <div style="font-size:17px;font-weight:700">Medicaid Myths</div>
    <div style="font-size:16px;font-weight:400;padding-left:18px">get the facts!</div>
  </div>
  <div class="abs stripe" style="left:17px;top:91px;width:200px"></div>
  <div class="abs myths" style="left:18px;top:117px;width:202px">
    <p>Most people know someone who has qualified for Medicaid, so there are a ton of myths out there about what is required to qualify. You wouldn’t take medical advice from a plumber, so don’t take legal advice from non-lawyers. Below are some of the common myths we hear.</p>
    <p class="myth">You earn too much money to be on Medicaid.</p>
    <p>Myth! If gross monthly earnings are above the $2,205 income cap, you need a Qualified Income Trust.</p>
    <p class="myth">Medicaid is a program for poor people.</p>
    <p>Wrong! Most middle class families can benefit from planning for Medicaid.</p>
    <p class="myth">The state will take your home if you die on Medicaid.</p>
    <p>Not Completely True! Texas will not take your home automatically, and if you plan properly, Texas probably never will. If you do not plan, though, the house is likely at risk.</p>
    <p class="myth">You need to give all your stuff away so that you’re so broke, you qualify for Medicaid.</p>
    <p>This is possibly the worst thing you can do! Making uncompensated transfers will cause penalties that may even prevent eligibility.</p>
    <p class="myth">You cannot leave your descendants an inheritance if you’re on Medicaid.</p>
    <p>Still Wrong! Medicaid recipients who plan properly can and usually do pass on an inheritance.</p>
    <p class="myth">You should sell your house, cash out life insurance, and liquidate every one of your assets.</p>
    <p>Please Don’t! You may not have to. Talk with an elder law attorney. You might be eligible for Medicaid right now and not even know it.</p>
  </div>

  <!-- Photo and planning columns -->
  <div class="photo" role="img" aria-label="Photo of a young caregiver and a smiling elderly woman giving thumbs up" style="left:233px;top:0;width:466px;height:274px;background:linear-gradient(120deg,#e9e4dc,#d8c3b2 40%,#b48e7c 70%,#6e6d76)"></div>
  <div class="abs brand" style="left:620px;top:18px;width:80px">
    <span class="mark" style="font-size:30px">TRV</span>
    <span class="name" style="font-size:4px;margin-top:2px">TOLLIVER REYES &amp; VANCE</span>
  </div>
  <div class="abs stripe" style="left:233px;top:274px;width:466px"></div>

  <div class="abs body-copy" style="left:246px;top:291px;width:210px">
    <h3 style="font-size:10px;font-weight:700;color:var(--navy);margin-bottom:7px">WHAT IS MEDICAID PLANNING?</h3>
    <p>Medicaid Planning usually involves restructuring assets to meet federal and state law eligibility criteria so that your loved one can get the medical care he or she needs and deserves.</p>
    <h3 style="font-size:9px;font-weight:600;color:var(--navy);margin-top:10px">How Do You Qualify for Medicaid?</h3>
    <p style="margin-top:0">Generally speaking, only seven qualification rules exist. A Nursing Home Medicaid Applicant must:</p>
    <p style="padding-left:15px;margin-top:10px">1) be a resident of Texas<br>2) be a citizen of the United States<br>3) be at least 65 years old or disabled<br>4) be in a skilled nursing facility for 30 days<br>5) have a medical necessity for long term care<br>6) have less than $2,205 gross monthly income<br>7) have less than $2,000 in countable resources</p>
  </div>
  <div class="abs body-copy" style="left:478px;top:288px;width:210px">
    <p class="col-head">But, these seven rules have lots of exceptions.</p>
    <p style="margin-top:0">By knowing each of the exceptions, an elder law attorney can help you develop a Medicaid eligibility plan that will not only lead to Medicaid qualification but will also preserve the value of your loved one’s estate.</p>
    <p class="col-head" style="margin-top:10px">Is Anything Different if the Applicant is Married?</p>
    <p style="margin-top:0">Absolutely! Medicaid law has many provisions to ensure the healthy spouse of an ailing senior does not impoverish herself trying to afford her spouse’s medical care. When an ailing spouse applies for nursing home Medicaid, the healthier spouse still at home is able to take advantage of the income diversion rules. She can also use the protected resource amount rules. And sometimes, she can even expand the protected resource amount if her monthly income is not in excess of the minimum monthly maintenance needs allowance after utilizing the income diversion rules. Confused yet? No worries. Make an appointment today.</p>
  </div>
  <div class="abs navy-band" style="left:233px;top:498px;width:466px;height:37px;justify-content:space-around"><span class="phone">www.trvlawgroup.example</span><span class="phone">555 - 248 - 3071 Ext. 204</span></div>
</section>

<!-- Rack card -->
<section class="sheet" style="left:796px;top:286px;width:233px;height:539px">
  <div class="abs brand" style="left:0;top:12px;width:233px">
    <span class="mark" style="font-size:60px">TRV</span>
    <span class="name">TOLLIVER REYES &amp; VANCE</span>
  </div>
  <div class="photo" role="img" aria-label="Illustration of a stethoscope resting on a blue map of the southern United States" style="left:0;top:135px;width:233px;height:156px;background:linear-gradient(135deg,#cdd9ea,#5d8fcc 45%,#2c5a9a 75%,#1e3560)"></div>
  <div class="abs orange-band" style="left:0;top:291px;width:233px;height:47px">MINERAL. INTELLECTUAL. RESIDENTIAL.<br>COMMERCIAL. PROPERTY</div>
  <div class="abs body-copy centered" style="left:10px;top:353px;width:213px">
    <p>Don’t know how to pay for long term care? For starters, don’t pay more than you need to for legal advice. Call to make an appointment with <span class="accent">Marcus Doyle</span> at TRV today.</p>
  </div>
  <div class="abs stripe" style="left:12px;top:404px;width:208px"></div>
  <div class="abs body-copy centered" style="left:10px;top:416px;width:213px">
    <p>Call for an appointment at our Midtown address. We will also meet you on your terms, whether at a nursing facility or a place of your choosing.</p>
  </div>
  <div class="abs navy-band" style="left:0;top:460px;width:233px;height:38px"><span class="phone">555 - 248 - 3071 Ext. 204</span></div>
  <div class="abs contact" style="left:0;top:498px;width:233px;font-size:6.2px"><div>Visit us on the web at<br>www.trvlawgroup.example<br>email: mdoyle@trvlawgroup.example</div><div>Bayline Commerce Center<br>872 Alder St., Suite 310<br>Houston, TX 77099</div></div>
</section>

</body>
</html>
```